Painting services company needs a DL brochure about their services

We need a brochure describing our painting services including our logo and photos of work. The final design needs to be colourful, vibrant, and targeted to schools, aged care, commercial property maintenance clients.

```html
<!DOCTYPE html>
<html lang="en">
<head>
<meta charset="utf-8">
<title>Brightcoat Crew – DL Brochure</title>
<link href="https://fonts.googleapis.com/css2?family=Oswald:wght@500;600;700&family=Open+Sans:wght@400;600;700&display=swap" rel="stylesheet">
<style>
  :root{
    --blue:#2b44a0;
    --navy:#1b2a6e;
    --deep:#101a4a;
    --yellow:#f7e43c;
    --white:#ffffff;
    --page:#d8d9db;
    --photo-a:#8a97b3;
    --photo-b:#c9cfd9;
  }
  *{box-sizing:border-box;margin:0;padding:0}
  html,body{width:788px;height:1200px;overflow:hidden;background:var(--page)}
  body{font-family:"Open Sans",Arial,sans-serif;color:var(--white)}
  .canvas{position:relative;width:788px;height:1200px;background:var(--page)}
  .spread{position:absolute;left:0;width:788px;height:557px;display:grid;grid-template-columns:repeat(3,1fr);background:var(--blue);box-shadow:0 6px 18px rgba(0,0,0,.18)}
  .spread--outside{top:28px}
  .spread--inside{top:615px;grid-template-rows:46px 1fr}
  .panel{position:relative;display:flex;flex-direction:column;overflow:hidden}
  .panel + .panel{border-left:1px solid rgba(255,255,255,.12)}
  .headline{font-family:"Oswald",Arial,sans-serif;font-weight:600;font-style:italic;text-transform:uppercase;line-height:1.15}
  .hl-yellow{color:var(--yellow)}
  .hl-navy{color:var(--navy)}
  .body-copy{font-size:8.5px;line-height:1.5}
  .photo{background:linear-gradient(135deg,var(--photo-a),var(--photo-b))}
  .photo-row{display:flex;gap:4px;padding:0 14px}
  .photo-row .photo{flex:1;height:120px;border:2px solid var(--white)}
  .brand{display:flex;align-items:center;gap:8px}
  .brand__mark{width:14px;height:14px;background:var(--yellow)}
  .brand__name{font-family:"Oswald",Arial,sans-serif;font-weight:600;font-size:20px;color:var(--white);text-transform:uppercase;letter-spacing:.5px}
  .phone-pill{display:inline-flex;align-items:center;gap:8px;background:var(--navy);color:var(--white);font-family:"Oswald",Arial,sans-serif;font-weight:600;font-size:20px;padding:5px 16px;border-radius:4px}
  .phone-pill svg{width:16px;height:16px}
  .web{font-size:9px;color:var(--navy);font-weight:600}

  /* outside: flap */
  .flap{padding-top:24px}
  .flap .headline{font-size:16px;padding:0 18px;color:var(--white)}
  .flap .body-copy{padding:10px 18px 16px}
  .flap__callout{margin-top:18px;background:var(--yellow);padding:18px 18px;flex:1}
  .flap__callout .headline{font-size:16px;color:var(--navy);padding:0}
  .flap__foot{height:34px;background:var(--blue)}

  /* outside: back */
  .back{padding-top:24px}
  .back .brand{padding:0 18px}
  .back__address{font-size:8.5px;padding:8px 18px 18px;opacity:.9}
  .back__quote{margin-top:18px;flex:1;background:var(--yellow);padding:18px;text-align:center;display:flex;flex-direction:column;align-items:center;gap:10px}
  .back__quote .headline{font-size:19px;color:var(--navy)}

  /* outside: cover */
  .cover__hero{position:relative;height:300px;background:radial-gradient(circle at 60% 55%,#2d4aa3,var(--deep) 70%)}
  .cover__about{position:absolute;top:24px;left:16px;right:16px}
  .cover__about .headline{font-size:13px;color:var(--yellow);margin-bottom:6px}
  .cover__brand{position:absolute;left:16px;bottom:28px;background:var(--blue);padding:10px 14px;border:2px solid var(--white)}
  .cover__phone{height:44px;background:var(--blue);display:flex;align-items:center;justify-content:center;gap:8px;font-family:"Oswald",Arial,sans-serif;font-weight:600;font-size:20px;border-top:3px solid var(--yellow)}
  .cover__phone svg{width:16px;height:16px}
  .cover__title{flex:1;background:var(--yellow);display:flex;flex-direction:column;align-items:center;justify-content:center;text-align:center}
  .cover__title .kicker{font-size:20px;color:var(--navy)}
  .cover__title .main{font-size:34px;color:var(--blue);line-height:1}
  .cover__title .sub{font-family:"Oswald",Arial,sans-serif;font-weight:500;font-size:13px;color:var(--navy);margin-top:6px}

  /* inside */
  .inside-head{grid-column:1/4;display:flex;justify-content:space-around;align-items:center;border-bottom:3px solid var(--yellow);background:var(--navy)}
  .inside-head span{font-family:"Oswald",Arial,sans-serif;font-weight:700;font-size:20px;letter-spacing:6px;text-transform:uppercase}
  .inside-head span:nth-child(3){color:var(--yellow)}
  .service{padding-top:16px}
  .service__tag{margin:0 14px;background:var(--yellow);color:var(--navy);font-family:"Oswald",Arial,sans-serif;font-weight:600;font-size:11px;text-transform:uppercase;padding:5px 8px;line-height:1.25}
  .ticks{list-style:none;padding:12px 14px 12px 18px;display:flex;flex-direction:column;gap:7px}
  .ticks li{display:flex;gap:7px;font-size:9px;line-height:1.35;align-items:flex-start}
  .ticks svg{flex:none;width:13px;height:13px}
  .service__foot{margin-top:auto;background:var(--yellow);padding:14px}
  .service__foot .headline{font-size:16px;color:var(--navy)}
  .service__note{margin:12px 14px 16px;background:var(--white);color:var(--navy);padding:10px}
  .service__big-photo{margin:4px 14px 0;height:170px;border:2px solid var(--white)}
  .service__contact{margin-top:auto;padding:16px 14px 18px;display:flex;flex-direction:column;align-items:center;gap:8px}
  .service__contact .web{color:var(--white)}
</style>
</head>
<body>
<main class="canvas">

  <!-- Outside of the brochure -->
  <section class="spread spread--outside">
    <article class="panel flap">
      <h2 class="headline">We are a family run business with <span class="hl-yellow">over 40 years experience</span></h2>
      <p class="body-copy">We provide a full range of painting and coating services for schools, aged care homes and commercial property owners. Our crews work around your hours, keep sites clean and deliver a finish that lasts for years.</p>
      <div class="photo-row">
        <div class="photo" role="img" aria-label="Photo of a freshly painted commercial building exterior"></div>
        <div class="photo" role="img" aria-label="Photo of a heritage facade under repaint"></div>
      </div>
      <div class="flap__callout">
        <p class="headline">Remember, when you need painters for a commercial building, we are the painters with the right attitude</p>
      </div>
      <div class="flap__foot"></div>
    </article>

    <article class="panel back">
      <div class="brand"><span class="brand__mark"></span><span class="brand__name">Brightcoat Crew</span></div>
      <p class="back__address">P.O. Box 410, Elmvale, NSW 2150</p>
      <div class="photo-row">
        <div class="photo" role="img" aria-label="Photo of painters working on an industrial site"></div>
        <div class="photo" role="img" aria-label="Photo of painted storage tanks"></div>
      </div>
      <div class="back__quote">
        <p class="headline">Call or email us now<br>to get a fast quote!</p>
        <span class="phone-pill">
          <svg viewBox="0 0 24 24" aria-hidden="true"><path fill="currentColor" d="M6.6 10.8a15.1 15.1 0 0 0 6.6 6.6l2.2-2.2c.3-.3.7-.4 1-.2 1.1.4 2.3.6 3.6.6.6 0 1 .4 1 1V20c0 .6-.4 1-1 1A17 17 0 0 1 3 4c0-.6.4-1 1-1h3.5c.6 0 1 .4 1 1 0 1.3.2 2.5.6 3.6.1.3 0 .7-.2 1z"/></svg>
          1300 555 018
        </span>
        <p class="web">www.brightcoatcrew.com.au</p>
      </div>
    </article>

    <article class="panel cover">
      <div class="cover__hero" role="img" aria-label="Photo of a blue paint tin and roller">
        <div class="cover__about">
          <h3 class="headline">Brightcoat Crew</h3>
          <p class="body-copy">Brightcoat Crew is a specialist commercial painting contractor serving clients across Australia with careful preparation and quality coatings.</p>
        </div>
        <div class="cover__brand brand"><span class="brand__mark"></span><span class="brand__name">Brightcoat Crew</span></div>
      </div>
      <div class="cover__phone">
        <svg viewBox="0 0 24 24" aria-hidden="true"><path fill="var(--yellow)" d="M6.6 10.8a15.1 15.1 0 0 0 6.6 6.6l2.2-2.2c.3-.3.7-.4 1-.2 1.1.4 2.3.6 3.6.6.6 0 1 .4 1 1V20c0 .6-.4 1-1 1A17 17 0 0 1 3 4c0-.6.4-1 1-1h3.5c.6 0 1 .4 1 1 0 1.3.2 2.5.6 3.6.1.3 0 .7-.2 1z"/></svg>
        1300 555 018
      </div>
      <div class="cover__title">
        <p class="headline kicker">Friendly</p>
        <h1 class="headline main">Painting<br>Contractors</h1>
        <p class="sub">Commercial Painters in Australia</p>
      </div>
    </article>
  </section>

  <!-- Inside of the brochure -->
  <section class="spread spread--inside">
    <header class="inside-head"><span>Specialist</span><span>Painting</span><span>Contractors</span></header>

    <article class="panel service">
      <h3 class="service__tag">Commercial &amp; industrial painting services</h3>
      <ul class="ticks">
        <li><svg viewBox="0 0 16 16"><circle cx="8" cy="8" r="8" fill="var(--yellow)"/><path d="M4.5 8.2l2.3 2.3 4.7-4.8" stroke="var(--navy)" stroke-width="2" fill="none"/></svg>Pressure cleaning of building facades</li>
        <li><svg viewBox="0 0 16 16"><circle cx="8" cy="8" r="8" fill="var(--yellow)"/><path d="M4.5 8.2l2.3 2.3 4.7-4.8" stroke="var(--navy)" stroke-width="2" fill="none"/></svg>Painting of broad areas and trim on commercial interiors and exteriors</li>
        <li><svg viewBox="0 0 16 16"><circle cx="8" cy="8" r="8" fill="var(--yellow)"/><path d="M4.5 8.2l2.3 2.3 4.7-4.8" stroke="var(--navy)" stroke-width="2" fill="none"/></svg>Corrosion repairs and protective coatings for steel</li>
        <li><svg viewBox="0 0 16 16"><circle cx="8" cy="8" r="8" fill="var(--yellow)"/><path d="M4.5 8.2l2.3 2.3 4.7-4.8" stroke="var(--navy)" stroke-width="2" fill="none"/></svg>On-site spray painting</li>
        <li><svg viewBox="0 0 16 16"><circle cx="8" cy="8" r="8" fill="var(--yellow)"/><path d="M4.5 8.2l2.3 2.3 4.7-4.8" stroke="var(--navy)" stroke-width="2" fill="none"/></svg>Texture coatings</li>
        <li><svg viewBox="0 0 16 16"><circle cx="8" cy="8" r="8" fill="var(--yellow)"/><path d="M4.5 8.2l2.3 2.3 4.7-4.8" stroke="var(--navy)" stroke-width="2" fill="none"/></svg>After-hours and weekends available</li>
      </ul>
      <div class="photo-row">
        <div class="photo" role="img" aria-label="Photo of a painted warehouse interior"></div>
        <div class="photo" role="img" aria-label="Photo of a repainted shopfront"></div>
      </div>
      <div class="service__foot">
        <p class="headline">We have an impressive range of unique experience</p>
      </div>
    </article>

    <article class="panel service">
      <h3 class="service__tag">Floor preparation and coating services</h3>
      <ul class="ticks">
        <li><svg viewBox="0 0 16 16"><circle cx="8" cy="8" r="8" fill="var(--yellow)"/><path d="M4.5 8.2l2.3 2.3 4.7-4.8" stroke="var(--navy)" stroke-width="2" fill="none"/></svg>Diamond grinding</li>
        <li><svg viewBox="0 0 16 16"><circle cx="8" cy="8" r="8" fill="var(--yellow)"/><path d="M4.5 8.2l2.3 2.3 4.7-4.8" stroke="var(--navy)" stroke-width="2" fill="none"/></svg>Shot blasting</li>
        <li><svg viewBox="0 0 16 16"><circle cx="8" cy="8" r="8" fill="var(--yellow)"/><path d="M4.5 8.2l2.3 2.3 4.7-4.8" stroke="var(--navy)" stroke-width="2" fill="none"/></svg>Glue and surface removal</li>
        <li><svg viewBox="0 0 16 16"><circle cx="8" cy="8" r="8" fill="var(--yellow)"/><path d="M4.5 8.2l2.3 2.3 4.7-4.8" stroke="var(--navy)" stroke-width="2" fill="none"/></svg>Epoxy and polyurethane coatings</li>
        <li><svg viewBox="0 0 16 16"><circle cx="8" cy="8" r="8" fill="var(--yellow)"/><path d="M4.5 8.2l2.3 2.3 4.7-4.8" stroke="var(--navy)" stroke-width="2" fill="none"/></svg>Anti-slip coatings</li>
        <li><svg viewBox="0 0 16 16"><circle cx="8" cy="8" r="8" fill="var(--yellow)"/><path d="M4.5 8.2l2.3 2.3 4.7-4.8" stroke="var(--navy)" stroke-width="2" fill="none"/></svg>Epoxy floors for warehouse and workshop</li>
      </ul>
      <div class="photo-row">
        <div class="photo" role="img" aria-label="Photo of a green epoxy floor with safety markings"></div>
        <div class="photo" role="img" aria-label="Photo of a repainted school building"></div>
      </div>
      <p class="service__note body-copy">Brightcoat Crew is one of the few commercial painting contractors that offers a complete service, from surface preparation to final coat. We plan every job to suit your site, your budget and your timeline.</p>
    </article>

    <article class="panel service">
      <h3 class="service__tag">New construction painting services</h3>
      <ul class="ticks">
        <li><svg viewBox="0 0 16 16"><circle cx="8" cy="8" r="8" fill="var(--yellow)"/><path d="M4.5 8.2l2.3 2.3 4.7-4.8" stroke="var(--navy)" stroke-width="2" fill="none"/></svg>Painting of new buildings</li>
        <li><svg viewBox="0 0 16 16"><circle cx="8" cy="8" r="8" fill="var(--yellow)"/><path d="M4.5 8.2l2.3 2.3 4.7-4.8" stroke="var(--navy)" stroke-width="2" fill="none"/></svg>Internals and externals</li>
        <li><svg viewBox="0 0 16 16"><circle cx="8" cy="8" r="8" fill="var(--yellow)"/><path d="M4.5 8.2l2.3 2.3 4.7-4.8" stroke="var(--navy)" stroke-width="2" fill="none"/></svg>Spray painting and texture coatings</li>
      </ul>
      <div class="photo service__big-photo" role="img" aria-label="Photo of a freshly painted aged care corridor"></div>
      <div class="service__contact">
        <span class="phone-pill" style="background:var(--yellow);color:var(--navy)">
          <svg viewBox="0 0 24 24" aria-hidden="true"><path fill="currentColor" d="M6.6 10.8a15.1 15.1 0 0 0 6.6 6.6l2.2-2.2c.3-.3.7-.4 1-.2 1.1.4 2.3.6 3.6.6.6 0 1 .4 1 1V20c0 .6-.4 1-1 1A17 17 0 0 1 3 4c0-.6.4-1 1-1h3.5c.6 0 1 .4 1 1 0 1.3.2 2.5.6 3.6.1.3 0 .7-.2 1z"/></svg>
          1300 555 018
        </span>
        <p class="web">www.brightcoatcrew.com.au</p>
      </div>
    </article>
  </section>

</main>
</body>
</html>
```